serious, thorough, light and simple - that's my advice and mediations

My business card should combine my logo (uploaded file) and my homepage (https://fellor-mediation.webnestsite.com).

Contact Information for Business Card

Name: Sabine Fellor di Vanti
Phone: 076 412 58 94
mail: sfellor@postkiv.ch
web: www.fellor-di-vanti.ch

```html
<!DOCTYPE html>
<html lang="de">
<head>
<meta charset="utf-8">
<title>Wege im Dialog – Visitenkarte</title>
<link rel="stylesheet" href="https://fonts.googleapis.com/css2?family=Fira+Sans:wght@400;500&family=Great+Vibes&family=Roboto:wght@400&display=swap">
<style>
  :root {
    --backdrop: #e6e6e6;
    --card: #f4f4f3;
    --navy: #1f3a78;
    --teal: #154f5c;
    --green: #0b6a3c;
    --gold: #a8844f;
    --ink-navy: #1e3463;
    --white: #ffffff;
  }
  * { box-sizing: border-box; margin: 0; padding: 0; }
  html, body { width: 1200px; height: 576px; overflow: hidden; }
  body {
    background: var(--backdrop);
    position: relative;
    font-family: "Fira Sans", sans-serif;
  }
  .card {
    position: absolute;
    top: 138px;
    width: 484px;
    height: 293px;
    background: var(--card);
    overflow: hidden;
    box-shadow: 0 2px 6px rgba(0,0,0,0.18);
  }
  .card--front { left: 81px; }
  .card--back { left: 602px; }

  /* Front */
  .brand {
    position: absolute;
    left: 0; right: 0; top: 96px;
    display: flex;
    align-items: center;
    justify-content: center;
    gap: 14px;
  }
  .brand__dot {
    width: 26px; height: 26px;
    border-radius: 50%;
    background: var(--navy);
  }
  .brand__name {
    font-family: "Fira Sans", sans-serif;
    font-weight: 500;
    font-size: 38px;
    color: var(--gold);
    letter-spacing: 0.5px;
  }
  .front__url {
    position: absolute;
    left: 0; right: 0; top: 241px;
    text-align: center;
    font-size: 13px;
    color: var(--ink-navy);
  }
  .front__band {
    position: absolute;
    left: 0; right: 0; bottom: 0;
    height: 12px;
    background: linear-gradient(90deg, var(--navy), var(--green));
  }

  /* Back */
  .back__panel { position: absolute; inset: 0; }
  .contact {
    position: absolute;
    left: 32px; top: 104px;
    color: var(--white);
  }
  .contact__name {
    font-family: "Great Vibes", cursive;
    font-size: 23px;
    margin-bottom: 8px;
  }
  .contact__list { list-style: none; }
  .contact__item {
    display: flex;
    align-items: center;
    gap: 10px;
    font-family: "Roboto", sans-serif;
    font-size: 12.5px;
    line-height: 18px;
    padding-left: 11px;
  }
  .contact__icon { width: 11px; height: 11px; flex: none; }
  .brand--vertical {
    position: absolute;
    left: 392px; top: 146px;
    transform: translate(-50%, -50%) rotate(-90deg);
    gap: 10px;
    display: flex;
    align-items: center;
    white-space: nowrap;
  }
  .brand--vertical .brand__name { font-size: 30px; }
  .brand--vertical .brand__dot { width: 20px; height: 20px; }
</style>
</head>
<body>

<section class="card card--front" aria-label="Vorderseite">
  <div class="brand">
    <span class="brand__dot"></span>
    <span class="brand__name">Wege im Dialog</span>
  </div>
  <p class="front__url">https://fellor-mediation.webnestsite.com</p>
  <div class="front__band"></div>
</section>

<section class="card card--back" aria-label="Rückseite">
  <svg class="back__panel" width="484" height="293" viewBox="0 0 484 293">
    <defs>
      <linearGradient id="panelGradient" x1="0" y1="1" x2="1" y2="0">
        <stop offset="0" stop-color="#1f3a78"/>
        <stop offset="0.55" stop-color="#154f5c"/>
        <stop offset="1" stop-color="#0b6a3c"/>
      </linearGradient>
    </defs>
    <path d="M0 0 H287 Q246 146 260 293 H0 Z" fill="url(#panelGradient)"/>
    <path d="M287 0 Q246 146 260 293" fill="none" stroke="#a8844f" stroke-width="4"/>
  </svg>

  <div class="contact">
    <p class="contact__name">Sabine Fellor di Vanti</p>
    <ul class="contact__list">
      <li class="contact__item">
        <svg class="contact__icon" viewBox="0 0 12 12" fill="#fff"><path d="M1 4 Q6 0 11 4 L9.5 5.5 L8 4.5 V3.5 H4 V4.5 L2.5 5.5 Z M3 6 H9 L10 11 H2 Z"/></svg>
        <span>076 412 58 94</span>
      </li>
      <li class="contact__item">
        <svg class="contact__icon" viewBox="0 0 12 12" fill="#fff"><path d="M0.5 2.5 H11.5 V9.5 H0.5 Z" /><path d="M0.8 2.8 L6 7 L11.2 2.8" fill="none" stroke="#1a4566" stroke-width="1"/></svg>
        <span>sfellor@postkiv.ch</span>
      </li>
      <li class="contact__item">
        <svg class="contact__icon" viewBox="0 0 12 12" fill="none" stroke="#fff" stroke-width="1"><circle cx="6" cy="6" r="5"/><ellipse cx="6" cy="6" rx="2.2" ry="5"/><path d="M1 6 H11"/></svg>
        <span>www.fellor-di-vanti.ch</span>
      </li>
    </ul>
  </div>

  <div class="brand--vertical">
    <span class="brand__dot"></span>
    <span class="brand__name">Wege im Dialog</span>
  </div>
</section>

</body>
</html>
```